International Marketing Company - Web Design Project

kVesta is a well-funded start up in London developing an Online Marketing Platform for small businesses in Europe.

We require a large number of high quality business web designs for our business website builder. Our business websites are completely integrated into our Online Marketing systems and therefore it is important for designers to comply with our Design Guidelines.

This initial contest is a trial for us to open up the design process to top designers for the Builders vertical (e.g. Builders, Electricians, Plumbers, Flooring, etc.). We have implemented a base html structure and design and included them in the files.

Use your creativity to design new and fresh designs based on the included elements (e.g. testimonials, business description, etc).

We will award the stated prize money for the top three designs.

Any designers that submit designs we feel are of a high enough quality but do not make the top 3 could still be compensated and WILL be invited to participate in our next vertical competition.

Therefore, we encourage designers to submit as many designs as possible as we may award up to 25 designs.

Submissions will be reviewed daily and feedback provided where possible.

Designers who can also code will have the options to implement their designs for an additional fee.

Good luck!
Updates

There has been a mistake made in regard to the prize. Pixel Harbor should have it fixed soon.

1st place = £350
2nd place = £250
3rd Place = £150

Thanks,
Dorian
25/11/2011

UPDATE:

1st place will win £350
2nd place will win £250
3rd place will win £150

Everything else is as to the specification.

Thanks
Dorian

Target Market(s)

Builders, Electricians, Plumbers, Tradesman, Small construction companies

Industry/Entity Type

Business

Requirements
Must have
• Totally new designs based around the elements we want to show on each page.

We are looking for something different to the design we already have. But you can use that as a starting point.

Use the included files to see what is required for each page. Here is a brief outline:

Homepage - Testimonials, News, Business Description, Latest Projects and Call to action

About-Us - Team Summary, About the Business and a call to action

Projects Page - Project Details (Oage Title and description), Each project needs a title, content and 2 images.

Testimonials Page - The testifiers name and their comment

Contacts Page - Trovix Map, Company address, business hours, contact form and a call to action.

Please submit final designs in Photoshop or Fireworks format.

Each page has a set of elements. These element must feature in the design of that page. See supporting documents for page details.

All elements must be included in your design. Please do not add any extra element.

Professional look and feel
Nice to have
• Design variations:
Full width designs
Boxed Designs
With AND without carousels
OR static images
Good use of stock images.

Creative use of the elements, dont be restricted/influenced by the default design we have already

Designs based on the 960 grid

```html
<!DOCTYPE html>
<html lang="en">
<head>
<meta charset="utf-8">
<title>ZX Builders</title>
<link href="https://fonts.googleapis.com/css2?family=Arimo:ital,wght@0,400;0,700;1,700&display=swap" rel="stylesheet">
<style>
:root{
  --blue:#2a76b8;
  --blue-dark:#1d5f9c;
  --text:#2b2b2b;
  --grey:#8a8a8a;
  --grey-light:#b9b9b9;
  --band:#eeeef0;
  --sand:#efebe7;
  --green:#b6d431;
  --orange:#f39a1e;
  --nav-top:#6a6a6a;
  --nav-bottom:#3c3c3c;
}
*{margin:0;padding:0;box-sizing:border-box}
html,body{width:1200px;height:990px;overflow:hidden;background:#fff}
body{font-family:"Arimo",Arial,sans-serif;color:var(--text);position:relative}
.abs{position:absolute}

.top-band{left:0;top:108px;width:1200px;height:120px;background:#ecedf0}
.sand-band{left:0;top:228px;width:1200px;height:267px;background:var(--sand)}

.logo{left:163px;top:29px}
.logo-name{font-size:23px;color:var(--blue);line-height:26px}
.logo-tag{font-size:18px;color:#666;line-height:22px}

.call{left:854px;top:42px;color:#a9a9a9}
.call-label{font-size:23px;line-height:26px}
.call-number{font-size:16px;font-weight:700;line-height:22px;margin-top:2px}
.call-icon{left:976px;top:38px}

.nav{left:149px;top:108px;width:903px;height:50px;background:linear-gradient(var(--nav-top),var(--nav-bottom));display:flex;align-items:center;padding-left:12px}
.nav a{color:#fff;text-decoration:none;font-size:13px;padding:0 20px;height:36px;line-height:36px;margin-right:0}
.nav a.active{background:linear-gradient(#3a86cb,var(--blue-dark));padding:0 19px}

.hero{left:149px;top:165px;width:574px;height:320px;background:linear-gradient(#4f76b5 0%,#5b80bd 55%,#b8744d 80%,#9b5e3e 100%)}

.welcome-strip{left:723px;top:163px;width:21px;height:322px;background:linear-gradient(90deg,#c4d8ea,#e6eef5)}
.welcome{left:744px;top:163px;width:307px;height:322px;background:linear-gradient(#f4f6f8,#c9d9e6)}
.welcome-head{height:64px;background:linear-gradient(#4a95d3,var(--blue-dark));color:#fff;font-size:24px;padding:20px 0 0 21px;letter-spacing:.2px}
.welcome p{font-size:13.4px;line-height:16.3px;color:#222;padding:7px 18px 0 21px}
.welcome a{color:#222}
.reach{left:994px;top:426px}

.work-title{left:151px;top:503px;font-size:18px;font-weight:700;color:var(--blue)}
.work{left:149px;top:523px;width:903px;height:144px;background:var(--band)}
.work-item{position:absolute;top:13px;width:157px}
.work-photo{width:157px;height:105px}
.work-cap{font-size:10.5px;color:#5a8fc2;margin-top:4px;text-align:center}
.kitchen{background:linear-gradient(135deg,#8a4a22,#c98a4e 50%,#5d3a20)}
.bedroom{background:linear-gradient(135deg,#a98760,#e6e1dc 55%,#6b6a86)}
.lounge{background:linear-gradient(135deg,#d4b27a,#6e4a2c 55%,#c5b7a2)}
.conservatory{background:linear-gradient(135deg,#b8845a,#d9d7de 55%,#6a3b2a)}

.rule{left:149px;width:903px;height:1px;background:#d6d6d6}

.col h2{font-weight:400;font-size:20px;color:var(--blue);text-decoration:underline;text-underline-offset:3px;margin-bottom:16px}
.col p{font-size:13px;line-height:18.3px;color:#333}
.col a{color:var(--orange);text-decoration:none}
.col .who{font-weight:700;color:var(--grey);font-size:13px;letter-spacing:.5px;margin:2px 0 14px}

.cta-box{left:822px;top:683px;width:230px;height:124px;background:var(--green);border-radius:26px}
.cta-tail{left:946px;top:806px}
.cta-script{left:830px;top:693px;width:72px;height:42px;border-radius:6px;background:#c9e05f}
.cta-phone{left:838px;top:738px}
.cta-text{left:917px;top:699px;width:130px;font-size:11.4px;line-height:14.5px;color:#333}
.cta-text strong{color:#fff;font-size:13px}
.cta-more{left:920px;top:775px;font-size:14px;font-weight:700;font-style:italic;color:var(--blue)}

.foot{top:936px;font-size:10.5px;line-height:14.5px;color:#444}
.foot a{color:#444}
</style>
</head>
<body>
<div class="abs top-band"></div>
<div class="abs sand-band"></div>

<header>
  <div class="abs logo">
    <div class="logo-name">Your Logo</div>
    <div class="logo-tag">And Tag line</div>
  </div>
  <div class="abs call">
    <div class="call-label">Call us on:</div>
    <div class="call-number">020 1234 5678</div>
  </div>
  <svg class="abs call-icon" width="72" height="56" viewBox="0 0 72 56" aria-hidden="true">
    <defs><linearGradient id="ph" x1="0" y1="0" x2="0" y2="1"><stop offset="0" stop-color="#f2f2f2"/><stop offset="1" stop-color="#c9c9c9"/></linearGradient></defs>
    <path d="M6 20 Q6 6 36 6 Q66 6 66 20 L66 26 L52 26 L52 18 L20 18 L20 26 L6 26 Z" fill="url(#ph)" stroke="#c4c4c4"/>
    <path d="M18 26 L54 26 L64 50 L8 50 Z" fill="url(#ph)" stroke="#c4c4c4"/>
    <circle cx="36" cy="38" r="7" fill="#e0e0e0" stroke="#c4c4c4"/>
  </svg>
</header>

<nav class="abs nav">
  <a class="active" href="#">Home</a>
  <a href="#">About us</a>
  <a href="#">Testimonials</a>
  <a href="#">Portfolio</a>
  <a href="#">Contact</a>
</nav>

<div class="abs hero" role="img" aria-label="Builder in a blue hard hat laying bricks against a blue sky"></div>

<div class="abs welcome-strip"></div>
<section class="abs welcome">
  <h1 class="welcome-head">Welcome to ZX Builders</h1>
  <p>Lorem ipsum dolor sit amet, consectetuer adipiscing elit, sed diam nonummy nibh euismo. Etiam varius sapien in turpis. Suspendisse eros nibh, cursus vel, malesuada id, ullamcorper.Lorem ipsum dolor sit amet, consectetuer adipiscing elit, sed diam nonummy nibh euismod.<br><a href="#">Read more about us.</a></p>
</section>
<svg class="abs reach" width="68" height="80" viewBox="0 0 68 80" role="img" aria-label="Reach us corner tab">
  <ellipse cx="34" cy="74" rx="34" ry="4" fill="#cfcfcf"/>
  <path d="M0 68 L68 0 L68 68 Z" fill="var(--blue)"/>
  <path d="M58 0 L68 0 L68 10 Z" fill="#175488"/>
</svg>

<h2 class="abs work-title">SEE OUR LATEST WORK</h2>
<section class="abs work">
  <div class="work-item" style="left:20px"><div class="work-photo kitchen" role="img" aria-label="Restored wooden kitchen"></div><div class="work-cap">House restoration in Crawley</div></div>
  <div class="work-item" style="left:249px"><div class="work-photo bedroom" role="img" aria-label="Restored bedroom with fitted wardrobes"></div><div class="work-cap">House restoration in Crawley</div></div>
  <div class="work-item" style="left:498px"><div class="work-photo lounge" role="img" aria-label="Restored living room"></div><div class="work-cap">House restoration in Crawley</div></div>
  <div class="work-item" style="left:727px"><div class="work-photo conservatory" role="img" aria-label="Restored conservatory with leather sofa"></div><div class="work-cap">House restoration in Crawley</div></div>
</section>
<div class="abs rule" style="top:672px"></div>

<section class="abs col" style="left:150px;top:684px;width:296px">
  <h2>Customers say</h2>
  <p>Quisque gravida. In quam. Donec blandit. Etiam dictum euismod lectus.Vestibulum tincidunt, erat vel molestie gravida, ligula lacus pulvinar sem, eu tincidunt magna nulla eu turpis... <a href="#">more</a></p>
  <p class="who">Mr John Doe</p>
  <p>Vestibulum tincidunt, erat vel molestie gravida, ligula lacus pulvinar sem, eu tincidunt magna... <a href="#">more</a></p>
  <p class="who">Mr Smith</p>
</section>

<section class="abs col" style="left:458px;top:684px;width:290px">
  <h2>Latest News</h2>
  <p>Quisque gravida. In quam. Donec blandit. Etiam dictum euismod lectus.Vestibulum tincidunt, erat vel molestie gravida, ligula lacus pulvinar sem, eu tincidunt magna nulla.. <a href="#">more</a></p>
  <p style="margin-top:9px">Donec blandit. Etiam dictum euismod lectus.Vestibulum tincidunt, erat vel molestie gravida, ligula lacus pulvinar sem, eu tincidunt magna nulla eu turpis..<a href="#">more</a></p>
</section>

<aside>
  <div class="abs cta-box"></div>
  <svg class="abs cta-tail" width="30" height="30" viewBox="0 0 30 30" aria-hidden="true"><path d="M0 0 L30 0 L2 28 Z" fill="var(--green)"/></svg>
  <div class="abs cta-script" role="img" aria-label="Call us now lettering"></div>
  <svg class="abs cta-phone" width="70" height="48" viewBox="0 0 70 48" aria-hidden="true">
    <path d="M4 16 Q4 4 35 4 Q66 4 66 16 L66 22 L52 22 L52 15 L18 15 L18 22 L4 22 Z" fill="#d3e680"/>
    <path d="M16 22 L54 22 L62 44 L8 44 Z" fill="#d3e680"/>
    <circle cx="35" cy="33" r="6" fill="#c2da57"/>
  </svg>
  <p class="abs cta-text">Call us on 0123456789 now to discuss how we can help you. My quotes are always <strong>FREE</strong> with no obligation.</p>
  <a class="abs cta-more" href="#">More info</a>
</aside>

<div class="abs rule" style="top:912px"></div>
<footer>
  <p class="abs foot" style="left:149px">© My Company.</p>
  <p class="abs foot" style="left:261px">Managed by kVesta</p>
  <p class="abs foot" style="left:387px"><a href="#">Admin Access</a></p>
  <p class="abs foot" style="left:771px">Phone: (+44) 20 7946 0182<br>E-mail: hello@zxbuilders.example</p>
  <p class="abs foot" style="left:958px">Northgate Works Ltd.<br>14 Brickfield Lane<br>RH10 1AB Crawley</p>
</footer>
</body>
</html>
```